Local Self Storage Company needs a namecard

We need to have a namecard designed out based on the attached logo.

to have a very simple yet modern namecard design to show to others that we are a company that provides self storage and event logistics

Design to be in the format of Ai, PSD and Jpeg when selected

Target Market(s)

customers who are moving house or office
companies that need to have bigger spaces for storage
both for short term or long term

Industry/Entity Type

Self Storage

Requirements
Must have
• The front of the namecard to just have the logo and tag line

The back of the namecard to input the information as:
XX (Name)
XXX (Title)
XX(Hp)
41 Crestmoor Lane, Velmar Industrial Building,
#03-09 Singapore 512694

```html
<!DOCTYPE html>
<html lang="en">
<head>
<meta charset="utf-8">
<title>Stowhaven Namecard</title>
<link rel="stylesheet" href="https://fonts.googleapis.com/css2?family=Ubuntu:wght@400;500;700&display=swap">
<style>
  :root {
    --brand-green: #6cb33f;
    --brand-blue: #1f4fa0;
    --muted-grey: #7a7d80;
    --card-white: #ffffff;
    --backdrop: #e9e6e1;
    --card-shadow: rgba(40, 30, 20, 0.22);
  }
  html, body {
    margin: 0;
    padding: 0;
    width: 1200px;
    height: 1000px;
    overflow: hidden;
    background: var(--backdrop);
    font-family: "Ubuntu", sans-serif;
  }
  .canvas {
    position: relative;
    width: 1200px;
    height: 1000px;
  }
  .card {
    position: absolute;
    width: 560px;
    height: 320px;
    background: var(--card-white);
    box-shadow: 0 10px 30px var(--card-shadow);
    overflow: hidden;
  }
  .card--front { left: 80px; top: 120px; }
  .card--back  { left: 560px; top: 540px; }

  .brand {
    display: flex;
    align-items: center;
    gap: 14px;
  }
  .brand__dot {
    width: 40px;
    height: 40px;
    border-radius: 50%;
    background: var(--brand-blue);
    flex: none;
  }
  .brand__text { display: flex; flex-direction: column; }
  .brand__name {
    font-family: "Ubuntu", sans-serif;
    font-weight: 500;
    font-size: 36px;
    line-height: 1.05;
    color: var(--brand-blue);
  }
  .brand__tagline {
    font-family: "Ubuntu", sans-serif;
    font-weight: 400;
    font-size: 14px;
    color: var(--muted-grey);
    margin-top: 4px;
  }

  .card--front .brand {
    position: absolute;
    left: 60px;
    top: 50%;
    transform: translateY(-50%);
  }

  .card--back .brand {
    position: absolute;
    right: 36px;
    top: 34px;
  }
  .brand--small .brand__dot { width: 30px; height: 30px; }
  .brand--small .brand__name { font-size: 26px; }
  .brand--small .brand__tagline { font-size: 11px; }

  .contact {
    position: absolute;
    left: 40px;
    bottom: 30px;
    font-family: "Ubuntu", sans-serif;
    font-size: 16px;
    line-height: 1.4;
    color: var(--brand-green);
  }
  .contact p { margin: 0; }
  .contact__name {
    font-weight: 500;
    font-size: 22px;
    letter-spacing: 1px;
    color: var(--brand-blue);
    text-transform: uppercase;
  }
  .contact__title {
    font-weight: 700;
    font-size: 16px;
    color: var(--brand-green);
    margin-bottom: 10px !important;
  }
  .contact__label { color: var(--brand-blue); font-weight: 500; }
</style>
</head>
<body>
<main class="canvas">
  <section class="card card--front" aria-label="Namecard front">
    <div class="brand">
      <span class="brand__dot"></span>
      <div class="brand__text">
        <span class="brand__name">Stowhaven</span>
        <span class="brand__tagline">Space when you need it</span>
      </div>
    </div>
  </section>

  <section class="card card--back" aria-label="Namecard back">
    <div class="brand brand--small">
      <span class="brand__dot"></span>
      <div class="brand__text">
        <span class="brand__name">Stowhaven</span>
        <span class="brand__tagline">Space when you need it</span>
      </div>
    </div>
    <div class="contact">
      <p class="contact__name">Daniel Koh</p>
      <p class="contact__title">Operations Director</p>
      <p><span class="contact__label">Hp:</span> +65 9184 3626</p>
      <p><span class="contact__label">Address:</span> 41 Crestmoor Lane, Velmar</p>
      <p>Industrial Building, #03-09</p>
      <p>Singapore 512694</p>
    </div>
  </section>
</main>
</body>
</html>
```